Lantern Above the Harbor ~ An Unbinding Passage for Versemakers

My book is called “Lantern Above the Harbor.” Its subtitle is “An Unbinding Passage for Versemakers.” It is a book about being a poet, writing poetry, and the ways in which poets are connected to both society and the central energy of the Universe. I want the cover design to be abstract and impressionistic. A suggestion of fireworks or a starburst would be a plus. To be consistent with the 3 other books I have published, I want the font for the title, as well as my name (Dorothea Halvik) to be Papyrus. The subtitle font can be something more plain and sans serif, like Arial or Franklin Gothic Book, probably in italics. As for color, I definitely want pale gold (angelic). Possible other complimentary colors could be either light or dark shades of gray, turquoise, rose, rust or red. I'm attaching the back cover text and also three pages from inside the book that have line drawings, to give an example of the interior artwork.
Updates

Forgot to mention: My book is a paperback. Its size will be 8.5" high and 5.5" wide. I'm self-publishing it, and it will be printed by Quillby Press in Nebraska, USA. It has 104 pages. I think you need the number of pages, in order to make the spine of the book the correct width.

Target Market(s)

My target market is people who write poetry or are interested in how poetry is written.

Industry/Entity Type

Poetry

Font styles to use
Sans Serif
Other font styles liked:
• Papyrus for the front cover. Arial or another sans serif font on the back cover.

Colors

Designer to choose colors to be used in the design.

Requirements
Must have
• My book cover needs to be inspiring and uplifting, as well as abstract and impressionistic, with kind of a "New Age" feel. I don't want anything that looks rigid and scholarly.
Nice to have
• The book talks about the connection poets have to the Universe and the Creative Energy at the center of everything. The cover should convey that Energy.
Should not have
• My cover should not be realistic, logical or straight-laced. I want something that feels free, imaginative and unfettered.

```html
<!DOCTYPE html>
<html lang="en">
<head>
<meta charset="utf-8">
<title>Lantern Above the Harbor — Dorothea Halvik</title>
<link rel="stylesheet" href="https://fonts.googleapis.com/css2?family=Fraunces:ital,opsz,wght@0,9..144,700;1,9..144,500&family=Libre+Baskerville&family=Oswald:wght@500&display=swap">
<style>
  :root {
    --cream: #f3ece0;
    --cream-deep: #ece1cf;
    --gold: #d9bf7e;
    --gold-pale: #e8d6a4;
    --turquoise: #7fc1bd;
    --rose: #eeb3a6;
    --rust: #c9523f;
    --charcoal: #4a4647;
    --ink: #1e1414;
    --wine: #8a1c2a;
    --rule: #c9ad6a;
  }
  html, body {
    margin: 0;
    padding: 0;
    overflow: hidden;
    background: var(--cream);
  }
  .cover {
    position: relative;
    width: 678px;
    height: 1200px;
    overflow: hidden;
    background: var(--cream);
  }
  .cover__artwork {
    position: absolute;
    inset: 0;
    background:
      radial-gradient(ellipse 36% 40% at 50% 46%, var(--cream) 60%, rgba(243,236,224,0) 100%),
      radial-gradient(ellipse 30% 30% at 50% 12%, var(--gold-pale) 0%, rgba(232,214,164,0) 100%),
      radial-gradient(ellipse 26% 50% at 4% 30%, var(--charcoal) 0%, rgba(74,70,71,0) 70%),
      radial-gradient(ellipse 30% 60% at 12% 55%, var(--turquoise) 0%, rgba(127,193,189,0) 80%),
      radial-gradient(ellipse 30% 22% at 10% 92%, var(--gold) 0%, rgba(217,191,126,0) 80%),
      radial-gradient(ellipse 40% 40% at 95% 15%, var(--rose) 0%, rgba(238,179,166,0) 80%),
      radial-gradient(ellipse 34% 30% at 96% 45%, #e9a08e 0%, rgba(233,160,142,0) 80%),
      radial-gradient(ellipse 40% 24% at 85% 90%, var(--rust) 0%, rgba(201,82,63,0) 80%),
      radial-gradient(ellipse 30% 20% at 60% 85%, var(--turquoise) 0%, rgba(127,193,189,0) 80%),
      var(--cream-deep);
  }
  .cover__title {
    position: absolute;
    left: 0;
    width: 678px;
    top: 236px;
    margin: 0;
    text-align: center;
    font-family: "Fraunces", Georgia, serif;
    font-weight: 700;
    color: var(--ink);
    line-height: 1;
  }
  .cover__title-main {
    display: block;
    font-size: 56px;
    letter-spacing: 0.5px;
  }
  .cover__title-link {
    display: block;
    font-size: 24px;
    font-style: italic;
    font-weight: 500;
    margin: 10px 0 10px;
  }
  .cover__subtitle {
    position: absolute;
    left: 0;
    width: 678px;
    top: 482px;
    margin: 0;
    text-align: center;
    font-family: "Libre Baskerville", Georgia, serif;
    font-size: 21px;
    line-height: 32px;
    color: var(--wine);
  }
  .cover__rule {
    position: absolute;
    left: 244px;
    top: 583px;
    width: 192px;
    height: 1px;
    background: var(--rule);
  }
  .cover__author {
    position: absolute;
    left: 0;
    width: 678px;
    top: 664px;
    margin: 0;
    text-align: center;
    font-family: "Oswald", Arial, sans-serif;
    font-weight: 500;
    font-size: 25px;
    letter-spacing: 0.5px;
    color: var(--ink);
  }
</style>
</head>
<body>
  <main class="cover">
    <div class="cover__artwork" role="img" aria-label="Abstract watercolor marbling in turquoise, charcoal, rose, rust and pale gold with fine gold veins and gold starbursts framing a cream center"></div>

    <h1 class="cover__title">
      <span class="cover__title-main">Lantern</span>
      <span class="cover__title-link">Above the</span>
      <span class="cover__title-main">Harbor</span>
    </h1>

    <p class="cover__subtitle">An Unbinding<br>Passage for<br>Versemakers</p>
    <div class="cover__rule"></div>

    <p class="cover__author">DOROTHEA HALVIK</p>
  </main>
</body>
</html>
```